Letterhead & Business Card for our Professional Practice (Financial Services)

We are looking for someone to design a letterhead and business card for our business, which is a professional practice called Corvel Brook Capital Limited. The website is at www.corvelbrookcapitel.example.

The letterhead needs to have: (a) our logo (b) address (c) telephone number (d) email address and (e) our company number.

We would like the stationary to be consistent with the website.

I have attached the logo in EPS and PNG format.

Target Market(s)

Professional services, large commercial enterprises, financial services

Industry/Entity Type

Financial Service

Font styles to use
Serif

Colors
3176b5
f04a50

Requirements
Must have
• Be consistent with our website located at www.corvelbrookcapital.example
• Be in the following formats:
• 1. Word template for the letterhead
• 2. PDF for the letterhead with setup and bleeds required at www.presslyne88.example
• 3. PDF for the business card with setup and bleeds required at www.presslyne88.example
Nice to have
• Something with a really interesting design that says "these guys are professional but dynamic and interesting"
Should not have
• Boring

```html
<!DOCTYPE html>
<html lang="en">
<head>
<meta charset="utf-8">
<title>Corvel Brook Capital – Stationery</title>
<link rel="stylesheet" href="https://fonts.googleapis.com/css2?family=Source+Serif+4:opsz,wght@8..60,400;8..60,600&display=swap">
<style>
  :root {
    --stage: #cbcbcb;
    --paper: #ffffff;
    --blue: #3176b5;
    --red: #f04a50;
    --ink: #1f3d63;
    --muted: #6b6f7a;
    --rule: #e3e3e6;
  }
  * { box-sizing: border-box; margin: 0; padding: 0; }
  html, body { width: 1200px; height: 1054px; overflow: hidden; }
  body { background: var(--stage); position: relative; font-family: "Source Serif 4", serif; color: var(--ink); }

  .letterhead, .card { position: absolute; background: var(--paper); overflow: hidden; box-shadow: 0 0 1px rgba(0,0,0,.15); }
  .letterhead { left: 168px; top: 121px; width: 574px; height: 811px; }

  .brand { position: absolute; display: flex; align-items: center; gap: 14px; }
  .brand-mark { background: var(--red); flex: none; }
  .brand-name { font-family: "Source Serif 4", serif; font-weight: 400; color: var(--blue); white-space: nowrap; line-height: 1; }

  .letterhead .brand { left: 0; right: 0; justify-content: center; top: 71px; }
  .letterhead .brand-mark { width: 48px; height: 48px; }
  .letterhead .brand-name { font-size: 25px; }

  .contact-list { position: absolute; list-style: none; font-weight: 400; }
  .contact-list li { display: flex; align-items: center; gap: 6px; white-space: nowrap; }
  .contact-list svg { flex: none; stroke: var(--red); fill: none; stroke-width: 1.3; }

  .letterhead .contact-list { left: 46px; top: 718px; font-size: 9px; }
  .letterhead .contact-list li { height: 13.5px; }
  .letterhead .contact-list svg { width: 9px; height: 9px; }

  .footer-band { position: absolute; left: 0; right: 0; bottom: 0; background: var(--blue); }
  .footer-web { position: absolute; right: 0; bottom: 0; background: var(--red); color: #fff;
    clip-path: polygon(6% 0, 100% 0, 100% 100%, 0 100%); display: flex; align-items: center; justify-content: center; }

  .letterhead .footer-band { height: 16px; }
  .letterhead .footer-web { width: 234px; height: 36px; font-size: 11px; padding-left: 10px; }

  .card { left: 784px; width: 248px; height: 149px; }
  .card-front { top: 220px; }
  .card-back { top: 389px; }

  .card-front .brand { left: 0; right: 0; top: 30px; flex-direction: column; gap: 10px; }
  .card-front .brand-mark { width: 44px; height: 44px; }
  .card-front .brand-name { font-size: 18px; }
  .tagline-band { position: absolute; left: 0; right: 0; bottom: 0; height: 20px; background: var(--blue);
    color: #fff; font-size: 5.5px; display: flex; align-items: center; justify-content: center; }

  .card-back .brand { left: 8px; width: 114px; top: 31px; flex-direction: column; gap: 10px; }
  .card-back .brand-mark { width: 48px; height: 48px; }
  .card-back .brand-name { font-size: 11.5px; }
  .card-divider { position: absolute; left: 127px; top: 24px; width: 1px; height: 84px; background: var(--rule); }
  .person { position: absolute; left: 143px; top: 28px; }
  .person-name { font-size: 10.5px; font-weight: 600; color: var(--red); }
  .person-title { font-size: 5.5px; color: var(--muted); margin-top: 1px; }
  .card-back .contact-list { left: 143px; top: 59px; font-size: 5.3px; }
  .card-back .contact-list li { min-height: 9.5px; align-items: flex-start; }
  .card-back .contact-list svg { width: 6px; height: 6px; margin-top: 1px; }
  .card-back .footer-band { height: 9px; }
  .card-back .footer-web { width: 129px; height: 19px; font-size: 6px; padding-left: 6px; }
</style>
</head>
<body>

<section class="letterhead" aria-label="Letterhead">
  <div class="brand">
    <span class="brand-mark"></span>
    <span class="brand-name">Corvel Brook Capital</span>
  </div>

  <ul class="contact-list">
    <li><svg viewBox="0 0 10 10"><path d="M2 1l2 2-1 1.5c.8 1.4 1.6 2.2 3 3L7.5 6l2 2-1.5 1.5C4.5 9 1 5.5.5 2z"/></svg>01632 960418</li>
    <li><svg viewBox="0 0 10 10"><rect x=".7" y="2" width="8.6" height="6"/><path d="M.7 2l4.3 3.5L9.3 2"/></svg>contact@corvelbrookcapital.example</li>
    <li><svg viewBox="0 0 10 10"><path d="M5 9.5S1.8 6 1.8 4a3.2 3.2 0 016.4 0C8.2 6 5 9.5 5 9.5z"/><circle cx="5" cy="4" r="1.1"/></svg>12-14 Riverside Row Ashmoor Westshire AB4 1ZZ</li>
    <li><svg viewBox="0 0 10 10"><rect x="1" y="1" width="8" height="8"/><path d="M3 4h4M3 6h4"/></svg>Company No. 09876543 · Registered in England and Wales</li>
  </ul>

  <div class="footer-band"></div>
  <div class="footer-web">www.corvelbrookcapital.example</div>
</section>

<section class="card card-front" aria-label="Business card front">
  <div class="brand">
    <span class="brand-mark"></span>
    <span class="brand-name">Corvel Brook Capital</span>
  </div>
  <div class="tagline-band">These guys are professional but dynamic and interesting</div>
</section>

<section class="card card-back" aria-label="Business card back">
  <div class="brand">
    <span class="brand-mark"></span>
    <span class="brand-name">Corvel Brook Capital</span>
  </div>
  <div class="card-divider"></div>
  <div class="person">
    <p class="person-name">Your name</p>
    <p class="person-title">Your Title</p>
  </div>
  <ul class="contact-list">
    <li><svg viewBox="0 0 10 10"><path d="M2 1l2 2-1 1.5c.8 1.4 1.6 2.2 3 3L7.5 6l2 2-1.5 1.5C4.5 9 1 5.5.5 2z"/></svg>01632 960418</li>
    <li><svg viewBox="0 0 10 10"><rect x=".7" y="2" width="8.6" height="6"/><path d="M.7 2l4.3 3.5L9.3 2"/></svg>contact@corvelbrookcapital.example</li>
    <li><svg viewBox="0 0 10 10"><path d="M5 9.5S1.8 6 1.8 4a3.2 3.2 0 016.4 0C8.2 6 5 9.5 5 9.5z"/><circle cx="5" cy="4" r="1.1"/></svg><span>12-14 Riverside Row Ashmoor<br>Westshire AB4 1ZZ</span></li>
  </ul>
  <div class="footer-band"></div>
  <div class="footer-web">www.corvelbrookcapital.example</div>
</section>

</body>
</html>
```